Packaging & Label Design for CDB Products

We are a European CBD company specialising in athletic recovery, sleep improvement and wellness.

We would like the packaging to incorporate our logo and name (and font 'Codec') 'Meridell CBD'. The design must be transferable to all of our products. CBD Oils, Balms, Lip Balm and Vape E-Liquid.

We would like it to be simple but eye-catching and modern. We don't want bright colours. Preferred pallet of muted greys, blacks, white and pastel colours. Geometric concepts, possibly using different colours for each item of the range, we are open to new and fresh ideas (we are seeking you for your experience) and when we find the right design we would likely throw more work in your direction..

Our product range is not complete so the designer must be flexible with some changes and provide files where format can be easily edited by packaging manufacturer. We are also waiting for dimensions for the labels and boxes for several products and will supply the designer with full dimensions of all products once selected.

Oil Box: 2.6 x 9.0 x 2.6 cm (open format 16.7 x 11.6cm)
Labels: 7.8 x 3.3 cm (Front and Back)

Our expected product range will be:
CBD Oil 1000mg
CBD Oil 3000mg
CBD Balm 100mg
CBD Balm 300mg
E-Liquid 500mg
Lip Balm 50mg

We look forward to seeing your ideas.

Best Regards
Meridell CBD

```html
<!DOCTYPE html>
<html lang="en">
<head>
<meta charset="utf-8">
<title>Meridell CBD – Label Range</title>
<link rel="stylesheet" href="https://fonts.googleapis.com/css2?family=Montserrat:wght@300;400;600&display=swap">
<style>
  :root {
    --page: #ffffff;
    --frame: #d2d2d2;
    --brand-block: #000000;
    --ink-light: #ffffff;
    --oil-1000: #c48c86;
    --oil-3000: #c4706a;
    --balm-100: #a2a97e;
    --balm-300: #8a9363;
    --eliquid-500: #8ab79f;
    --lipbalm-50: #b8ae9c;
  }
  * { box-sizing: border-box; margin: 0; padding: 0; }
  html, body {
    width: 1200px;
    height: 1200px;
    overflow: hidden;
    background: var(--page);
    font-family: "Montserrat", sans-serif;
  }
  .range {
    position: relative;
    width: 1200px;
    height: 1200px;
  }
  .label {
    position: absolute;
    width: 233px;
    height: 547px;
    border: 2px solid var(--frame);
    border-bottom: none;
  }
  .label--oil-1000    { left: 86px;  top: 35px; }
  .label--balm-100    { left: 460px; top: 37px; }
  .label--balm-300    { left: 835px; top: 37px; }
  .label--oil-3000    { left: 84px;  top: 619px; }
  .label--eliquid-500 { left: 467px; top: 619px; }
  .label--lipbalm-50  { left: 841px; top: 625px; }

  .brand-block {
    position: absolute;
    left: 30px;
    top: 35px;
    width: 168px;
    height: 168px;
    background: var(--brand-block);
    display: flex;
    flex-direction: column;
    align-items: center;
    justify-content: center;
    color: var(--ink-light);
    font-weight: 600;
    text-align: center;
  }
  .brand-mark {
    width: 26px;
    height: 26px;
    border: 2px solid var(--ink-light);
    border-radius: 50%;
    margin-bottom: 12px;
  }
  .brand-name {
    font-size: 15px;
    letter-spacing: 1.5px;
    line-height: 1;
  }
  .brand-sub {
    font-size: 8px;
    letter-spacing: 4px;
    margin-top: 4px;
    line-height: 1;
  }

  .product-block {
    position: absolute;
    left: 30px;
    top: 306px;
    width: 168px;
    height: 241px;
    color: var(--ink-light);
    text-align: center;
  }
  .label--oil-1000 .product-block    { background: var(--oil-1000); }
  .label--balm-100 .product-block    { background: var(--balm-100); }
  .label--balm-300 .product-block    { background: var(--balm-300); }
  .label--oil-3000 .product-block    { background: var(--oil-3000); }
  .label--eliquid-500 .product-block { background: var(--eliquid-500); }
  .label--lipbalm-50 .product-block  { background: var(--lipbalm-50); }

  .product-name {
    position: absolute;
    left: 0;
    right: 0;
    top: 74px;
    font-size: 27px;
    font-weight: 600;
    letter-spacing: 0.5px;
    line-height: 1;
    word-spacing: 4px;
  }
  .product-rule {
    position: absolute;
    left: 21px;
    width: 126px;
    top: 119px;
    height: 2px;
    background: var(--ink-light);
  }
  .product-strength {
    position: absolute;
    left: 0;
    right: 0;
    top: 139px;
    font-size: 21px;
    font-weight: 300;
    line-height: 1;
  }
</style>
</head>
<body>
<main class="range">

  <section class="label label--oil-1000">
    <div class="brand-block"><span class="brand-mark"></span><span class="brand-name">MERIDELL</span><span class="brand-sub">CBD</span></div>
    <div class="product-block">
      <h2 class="product-name">CBD OIL</h2>
      <div class="product-rule"></div>
      <p class="product-strength">1000mg</p>
    </div>
  </section>

  <section class="label label--balm-100">
    <div class="brand-block"><span class="brand-mark"></span><span class="brand-name">MERIDELL</span><span class="brand-sub">CBD</span></div>
    <div class="product-block">
      <h2 class="product-name">CBD BALM</h2>
      <div class="product-rule"></div>
      <p class="product-strength">100mg</p>
    </div>
  </section>

  <section class="label label--balm-300">
    <div class="brand-block"><span class="brand-mark"></span><span class="brand-name">MERIDELL</span><span class="brand-sub">CBD</span></div>
    <div class="product-block">
      <h2 class="product-name">CBD BALM</h2>
      <div class="product-rule"></div>
      <p class="product-strength">300mg</p>
    </div>
  </section>

  <section class="label label--oil-3000">
    <div class="brand-block"><span class="brand-mark"></span><span class="brand-name">MERIDELL</span><span class="brand-sub">CBD</span></div>
    <div class="product-block">
      <h2 class="product-name">CBD OIL</h2>
      <div class="product-rule"></div>
      <p class="product-strength">3000mg</p>
    </div>
  </section>

  <section class="label label--eliquid-500">
    <div class="brand-block"><span class="brand-mark"></span><span class="brand-name">MERIDELL</span><span class="brand-sub">CBD</span></div>
    <div class="product-block">
      <h2 class="product-name">E-LIQUID</h2>
      <div class="product-rule"></div>
      <p class="product-strength">500mg</p>
    </div>
  </section>

  <section class="label label--lipbalm-50">
    <div class="brand-block"><span class="brand-mark"></span><span class="brand-name">MERIDELL</span><span class="brand-sub">CBD</span></div>
    <div class="product-block">
      <h2 class="product-name">LIP BALM</h2>
      <div class="product-rule"></div>
      <p class="product-strength">50mg</p>
    </div>
  </section>

</main>
</body>
</html>
```